Flyer für Selbstwert-Coachin und Bewusstseinstrainerin
Der Flyer ist wunderschön, kreativ und edel geworden und wurde von der Designerin genau nach meinen Wünschen super umgesetzt! Ich bin sehr zufrieden und kann die Designerin Lunea2281 jedem nur empfehlen. Einfach Top!!! 1 A!!! Vielen herzlichen Dank!
Zielgruppe
Ich bin Selbstwert Coach und Bewusstseinstrainerin und möchte einen Flyer für mein neues Angebot 'Innenkraft Akademie für Jugendliche ab 16' gestalten lassen.
Die Zielgruppe sind Eltern von Jugendlichen in der Oberstufe, deren Kinder unter Schulstress und Leistungsdruck leiden und zu wenig Selbstbewusstsein haben.
Aufgabenstellung
Ich habe bereits das Titelbild bei Bildquell gesucht #739201584, bitte dieses nehmen, es kann auch ein ähnliches noch besseres vorgeschlagen werden.
Ich möchte einen ansprechenden, schönen, hochwertigen Flyer mit den Farben der Landingpage, gelb, blau, gold... und Bilder von Jugendlichen, dort wo Platz ist, ansprechend und klar. Bitte keine Schnörkel und 08 15 Figuren, das Auge soll hängen bleiben, der Flyer hängt straßenseitig. Dieser soll ein 6-seitiger Wickelfalz sein.

```html
<!DOCTYPE html>
<html lang="de">
<head>
<meta charset="utf-8">
<title>Innenkraft Akademie – Wickelfalz-Flyer</title>
<link href="https://fonts.googleapis.com/css2?family=Bebas+Neue&family=Open+Sans:ital,wght@0,400;0,600;0,700;1,400&display=swap" rel="stylesheet">
<style>
:root{
  --navy:#0c0c6e;
  --navy-dark:#07075a;
  --gold:#f6c400;
  --gold-soft:#fde9a0;
  --text:#3d3d3d;
  --page:#e9e9e9;
  --sheet:#ffffff;
  --rule:#c9c9c9;
}
*{margin:0;padding:0;box-sizing:border-box}
html,body{width:847px;height:1200px;overflow:hidden;background:var(--page)}
body{font-family:"Open Sans",Arial,sans-serif;color:var(--text)}
.stage{position:absolute;left:0;top:0;width:883px;height:1251px;transform:scale(.9593);transform-origin:0 0}
.sheet{position:absolute;left:105px;width:673px;height:479px;background:var(--sheet);border:1px solid var(--rule)}
.sheet--outer{top:121px}
.sheet--inner{top:651px}
.panel{position:absolute;top:0;width:224px;height:100%;overflow:hidden}
.panel + .panel{border-left:1px solid #ddd}
.p1{left:0}.p2{left:224px}.p3{left:448px;width:225px}
.photo{position:absolute;left:0;top:0;width:100%}
.heading{font-family:"Bebas Neue",Impact,sans-serif;color:var(--navy);letter-spacing:.3px;line-height:1}
.body{font-size:7.4px;line-height:1.55}
.body p{margin-bottom:5px}
.body--modules{font-size:7px;line-height:1.38;letter-spacing:-.1px}
.body--modules p{margin-bottom:3px}
.sub{font-family:"Open Sans",sans-serif;font-weight:700;color:var(--navy);font-size:11px}
.bold{font-weight:700}
ul.dots{list-style:none;margin:0 0 3px 6px}
ul.dots li{position:relative;padding-left:8px}
ul.dots li::before{content:"•";position:absolute;left:0}
.gold-line{position:absolute;left:0;width:100%;height:8px;background:linear-gradient(90deg,var(--gold),var(--gold-soft) 85%,#fff)}
.band{position:absolute;background:linear-gradient(90deg,var(--navy) 0%,var(--navy) 45%,rgba(12,12,110,.1) 100%)}
.band-title{font-family:"Bebas Neue",Impact,sans-serif;color:var(--gold);line-height:1}
.checks{list-style:none}
.checks li{position:relative;padding-left:12px;margin-bottom:7px;font-size:7.6px;line-height:1.45}
.checks svg{position:absolute;left:0;top:1px;width:10px;height:9px}
.wordmark{font-family:"Open Sans",sans-serif;font-weight:600;color:#b58a3a;font-size:11px;letter-spacing:.5px}
</style>
</head>
<body>
<div class="stage">

  <section class="sheet sheet--outer">
    <div class="panel p1">
      <div class="photo" role="img" aria-label="Foto: lachende Gruppe Jugendlicher" style="height:133px;background:linear-gradient(120deg,#5a6b55,#c9a98a 45%,#8a4a3e 75%,#3f3f45)"></div>
      <h2 class="heading" style="position:absolute;left:13px;top:141px;font-size:14px;width:200px">Hast du das Gefühl, deinem Kind wird alles zu viel?</h2>
      <div class="body" style="position:absolute;left:13px;top:178px;width:203px">
        <p>Leidet auch dein Kind an Schulstress, Leistungsdruck und hat zu wenig Selbstbewusstsein?</p>
        <p>Das Jugendalter ist eine wichtige, oft schwierig verlaufende Entwicklungsphase, in der sich Jugendliche selbst erfahren und finden dürfen. Durch den stressigen, durch Leistungsdruck geprägten Schulalltag wird die Psyche doppelt gefordert. Viele Jugendliche fühlen sich schlecht, wissen oft nicht mehr weiter, negative Gedanken und Ängste machen sich breit. Oft geht der Glaube an sich selbst verloren. Das Selbstbewusstsein und der eigene Selbstwert schwinden.<br>Ziel des begleitenden Coachings ist, die Jugendlichen zu befähigen, Herausforderungen des Lebens gut meistern und wieder Freude und Spaß am Leben empfinden zu können. Zu den Schwerpunkten zählt die Rückbesinnung auf sich selbst und die eigene Gefühlswelt, Persönlichkeitsentwicklung und die Anwendung der geistigen Gesetze.</p>
        <p>Der Lehrgang ist aktive Lebensschule, motiviert zur Freude an der Eigenverantwortung und Gestaltung eines glücklichen Lebens in körperlicher, geistiger und seelischer Gesundheit.</p>
      </div>
    </div>

    <div class="panel p2">
      <div class="photo" role="img" aria-label="Foto: Bücherstapel mit grünem Zweig" style="height:120px;background:linear-gradient(180deg,#f2f2f2,#e2e2e2 60%,#cfcfc8)"></div>
      <div class="band" style="left:0;top:120px;width:190px;height:31px"></div>
      <h2 class="band-title" style="position:absolute;left:15px;top:124px;font-size:26px">20 Module</h2>
      <div class="body body--modules" style="position:absolute;left:7px;top:156px;width:214px">
        <p><span class="bold">Innerhalb von 20 Modulen während des Schuljahres</span> werden einfache Übungen, Techniken und Methoden für den Alltag und die geistigen Lebensgesetze gelehrt und trainiert. Gemeinsam greifen wir Schwierigkeiten des täglichen Lebens auf und erarbeiten Lösungsmöglichkeiten.</p>
        <div class="sub" style="margin:0 0 2px;font-size:10px">INHALTE</div>
        <div class="bold">sich gut fühlen Dein Kind lernt,</div>
        <ul class="dots">
          <li>mit negativen Gedanken und Gefühlen umzugehen</li>
          <li>aus sich selbst Kraft und Energie zu tanken</li>
          <li>trotz Schulstress und Belastungen entspannt zu bleiben</li>
          <li>angstfreier und gelassener zu sein</li>
        </ul>
        <div class="bold">glücklich sein Dein Kind lernt,</div>
        <ul class="dots">
          <li>mit mentalen Bildern und Affirmationen zu arbeiten</li>
          <li>auf seine innere Stimme und sein Herz zu hören und zu vertrauen</li>
          <li>sein Leben glücklich und erfolgreich zu gestalten und zu erleben</li>
        </ul>
        <div class="bold">an sich glauben Dein Kind lernt,</div>
        <ul class="dots">
          <li>an sich und seine Fähigkeiten zu glauben und ein positives Bild von sich zu entwickeln</li>
          <li>selbstsicher, selbstbewusst und innerlich stark zu werden</li>
          <li>sich zu vertrauen und sich zutrauen, das zu sagen, was es denkt und fühlt, egal was Mitschüler/innen oder Freund/innen denken</li>
          <li>sich selbst zu mögen und sich so anzunehmen, wie es ist</li>
          <li>mit Konflikten umzugehen und Probleme schneller zu lösen</li>
        </ul>
      </div>
      <div class="gold-line" style="bottom:0"></div>
    </div>

    <div class="panel p3">
      <div class="photo" role="img" aria-label="Porträtfoto der Coachin" style="width:126px;height:112px;background:linear-gradient(135deg,#e8c9a0,#d9a97a 50%,#b9c6d8)"></div>
      <h2 class="heading" style="position:absolute;left:132px;top:10px;font-size:17px;width:92px;line-height:.98">Die Coachin<br>und<br>Vortragende</h2>
      <div style="position:absolute;left:126px;top:69px;width:99px;height:43px;background:var(--navy)"></div>
      <div class="body" style="position:absolute;left:7px;top:119px;width:215px;font-size:7.2px;line-height:1.5">
        <p><span class="bold">Lena Arnsteiner</span> leitet den schulbegleitenden Lehrgang Innenkraft Akademie. Sie ist gelernte Pädagogin für allgemeinbildende höhere Schulen für die Fächer Psychologie/Philosophie/Pädagogik und Bildnerische Erziehung. Als Selbstwert- und Selbstbewusstseins Coach, Mental- und Emotional Coach und Bewusstseinstrainerin begleitet sie seit 2006 Erwachsene und Jugendliche in ihrer Praxis sowie online.</p>
        <p>Sie zeigt Wege aus Krisen und vermittelt Tools und Werkzeug, das „Wie“ um das eigene Leben glücklich gestalten zu können</p>
        <div class="sub" style="margin:6px 0 2px">TERMINE</div>
        <p>Die 20 Module finden alle 2 Wochen immer dienstags (18.00 – ca. 20.00 Uhr oder länger) schulbegleitend statt und können nur insgesamt gebucht werden. (Terminänderungen vorbehalten)Die aktuellen Termine und Kosten für den gesamten Lehrgang finden Sie unter:<br><span class="bold">https://www.innenkraft-staerken.at/innenkraft-akademie/</span></p>
      </div>
      <div style="position:absolute;left:9px;top:393px;width:210px">
        <div class="sub" style="font-size:15px">ORT</div>
        <div style="font-size:12.5px;line-height:1.35;color:var(--text)">Der Lehrgang findet online via Meetwell statt.</div>
      </div>
      <div style="position:absolute;left:0;bottom:0;width:100%;height:22px;background:var(--navy)"></div>
    </div>
  </section>

  <section class="sheet sheet--inner">
    <div class="panel p1">
      <div class="photo" role="img" aria-label="Foto: jubelnde Jugendliche am Schreibtisch" style="height:152px;background:linear-gradient(120deg,#e9e4dc,#cfc3b2 45%,#a56a78 70%,#e7e2da)"></div>
      <h2 class="heading" style="position:absolute;left:15px;top:160px;font-size:22px">Vorteile und Nutzen</h2>
      <ul class="checks" style="position:absolute;left:15px;top:184px;width:200px">
        <li><svg viewBox="0 0 10 9"><path d="M1 5l3 3 5-7" fill="none" stroke="#4a4a4a" stroke-width="1.8"/></svg>Beste Prävention für die psychische Gesundheit, Steigerung des Wohlbefindens von Geist, Körper und Seele</li>
        <li><svg viewBox="0 0 10 9"><path d="M1 5l3 3 5-7" fill="none" stroke="#4a4a4a" stroke-width="1.8"/></svg>Konkrete Lösungsansätze bei auftretenden Konflikten, Schulproblemen und Mobbing</li>
        <li><svg viewBox="0 0 10 9"><path d="M1 5l3 3 5-7" fill="none" stroke="#4a4a4a" stroke-width="1.8"/></svg>Veränderter Umgang bzw. Reduktion von Überforderung, Leistungsdruck und Schulstress</li>
        <li><svg viewBox="0 0 10 9"><path d="M1 5l3 3 5-7" fill="none" stroke="#4a4a4a" stroke-width="1.8"/></svg>Persönlichkeitsentwicklung, Lernen fürs Leben</li>
        <li><svg viewBox="0 0 10 9"><path d="M1 5l3 3 5-7" fill="none" stroke="#4a4a4a" stroke-width="1.8"/></svg>Grundlagen zur Gestaltung eines glücklichen, erfolgreichen Lebens</li>
        <li><svg viewBox="0 0 10 9"><path d="M1 5l3 3 5-7" fill="none" stroke="#4a4a4a" stroke-width="1.8"/></svg>Stärkung von Selbstbewusstsein, Selbstvertrauen, Selbstliebe und Selbstwert</li>
      </ul>
      <h2 class="heading" style="position:absolute;left:15px;top:362px;font-size:17px;width:190px">Voraussetzungen für<br>die Teilnahme</h2>
      <div class="body" style="position:absolute;left:15px;top:399px;width:200px;font-size:7.8px">
        <p>Das wichtigste ist, dass dein Kind am Lehrgang teilnehmen will.</p>
        <p>Interesse, Neugierde und vor allem die Bereitschaft zur aktiven Umsetzung der Inhalte sind notwendig, um gute Ergebnisse zu erzielen.</p>
      </div>
    </div>

    <div class="panel p2">
      <div class="band" style="left:0;top:14px;width:185px;height:48px"></div>
      <h2 class="band-title" style="position:absolute;left:15px;top:20px;font-size:19px;line-height:1">Kontakt &amp;<br>Veranstalterin:</h2>
      <div style="position:absolute;left:14px;top:79px;color:var(--navy)">
        <div style="font-weight:600;font-size:12.5px">Mag. Lena Arnsteiner</div>
        <div style="font-size:7.6px">Selbstwert Coach, Bewusstseinstrainerin</div>
        <div style="font-size:8px;margin-top:17px;line-height:1.5"><span class="bold">E-Mail :</span>&nbsp; info@innenkraft-staerken.at<br><span class="bold">Mobil &nbsp;:</span>&nbsp; +43(0)650 318 2274</div>
      </div>
      <div role="img" aria-label="Rundes Porträtfoto der Veranstalterin" style="position:absolute;left:37px;top:191px;width:150px;height:150px;border-radius:50%;background:radial-gradient(circle at 45% 40%,#f0d3b4,#d9b07a 55%,#6d8a5a)"></div>
      <div class="wordmark" style="position:absolute;left:0;width:100%;top:420px;text-align:center">Lena Arnsteiner</div>
      <div class="gold-line" style="bottom:0"></div>
    </div>

    <div class="panel p3">
      <div class="photo" role="img" aria-label="Foto: lachende junge Frau mit Locken" style="height:236px;background:linear-gradient(135deg,#f4f1ea,#d8b58e 45%,#9a6a45 70%,#ece8e0)"></div>
      <div style="position:absolute;left:0;top:189px;width:100%;height:47px;background:linear-gradient(90deg,var(--navy) 0%,rgba(12,12,110,.9) 55%,rgba(12,12,110,.35) 100%)"></div>
      <div style="position:absolute;left:11px;top:194px;color:var(--gold)">
        <span class="band-title" style="font-size:19px;display:block">Innenkraft</span>
        <span class="band-title" style="font-size:19px">Akademie</span>
        <span style="font-size:8px"> für Jugendliche ab 16</span>
      </div>
      <div class="gold-line" style="top:236px;height:18px"></div>
      <div style="position:absolute;left:14px;top:283px;width:200px;font-size:9.2px;line-height:1.5">
        <p style="margin-bottom:9px">Schulbegleitender Praxis Lehrgang für mentale Stärke und Selbstbewusstsein</p>
        <p style="margin-bottom:9px">Schulstress &amp; Leistungsdruck bewältigen Selbstsicherer, gelassener &amp; angstfrei werden</p>
        <p>und dabei<br>ein starkes Selbstwertgefühl aufbauen und sich selbst vertrauen</p>
      </div>
      <div class="gold-line" style="top:421px"></div>
      <div style="position:absolute;left:0;top:429px;width:100%;height:50px;background:var(--navy);color:#fff;font-style:italic;font-size:8.6px;line-height:1.4;padding:6px 12px">Einfache Übungen, Techniken und Methoden für den Alltag und ein glückliches erfolgreiches Leben</div>
    </div>
  </section>

</div>
</body>
</html>
```